Flyer Design Project

Required:

A double sided A5 leaflet design

Purpose:

The purpose of this leaflet is as a marketing tool for a revolutionary phone call service from the UK. This revolutionary service provides unlimited phone calls to 40 international destinations for mobile phone users who opt into the service. This enables users to save money on their international telephone calls.

Target Market(s)

International Caller from the UK to the Indian Subcontinent, Europe, North America, Far East, Australia

Industry/Entity Type

Marketing

Requirements
Must have
• The design should include on the back page of the leaflet:

- Flags for each of the 40 destinations

- Clear clean and uncluttered design

- Clear easily readable font

```html
<!DOCTYPE html>
<html lang="en">
<head>
<meta charset="utf-8">
<title>Orbit Telecom – Unlimited Calls Leaflet</title>
<link href="https://fonts.googleapis.com/css2?family=Open+Sans:ital,wght@0,400;0,600;0,700;0,800;1,400;1,600&family=Noto+Sans:wght@400;500&display=swap" rel="stylesheet">
<style>
  :root {
    --blue: #1a5fb4;
    --deep-blue: #1c3f94;
    --red: #e41b23;
    --ink: #1d1d1d;
    --grey: #444;
    --cyan: #3fd3f2;
    --paper: #ffffff;
    --flag-red: #e8202a;
  }
  * { margin: 0; padding: 0; box-sizing: border-box; }
  html, body { width: 1200px; height: 863px; overflow: hidden; background: var(--paper); }
  body { font-family: "Open Sans", Arial, sans-serif; color: var(--ink); position: relative; }

  .page { position: absolute; top: 0; width: 600px; height: 863px; }
  .page--front { left: 0; }
  .page--back { left: 600px; }

  .brand { position: absolute; top: 20px; left: 40px; display: flex; align-items: center; gap: 8px;
           font-weight: 800; font-size: 28px; line-height: 36px; color: var(--deep-blue); }
  .brand__dot { width: 20px; height: 20px; border-radius: 50%; background: var(--blue); }

  .headline { position: absolute; left: 40px; top: 64px; width: 500px; color: var(--deep-blue);
              font-weight: 400; font-size: 46px; line-height: 58px; letter-spacing: -0.5px; }
  .headline strong { color: var(--red); font-weight: 800; }
  .headline .big-num { font-size: 56px; font-weight: 400; -webkit-text-stroke: 2px var(--red); color: transparent; }
  .headline-bang { position: absolute; left: 522px; top: 96px; font-size: 150px; font-weight: 800;
                   line-height: 150px; color: var(--red); }

  .section-title { position: absolute; left: 40px; color: var(--deep-blue); font-weight: 600; font-size: 16px; line-height: 22px; }
  .steps { position: absolute; left: 40px; list-style: none; color: var(--ink); }
  .steps b { color: var(--red); }
  .steps--front { top: 278px; font-size: 12px; line-height: 16.5px; }
  .steps--back { top: 100px; width: 540px; font-size: 12.3px; line-height: 18.3px; }
  .hl { color: var(--red); }
  .para { position: absolute; left: 40px; width: 530px; font-size: 12.3px; line-height: 18px; color: var(--ink); }

  .photo { position: absolute; left: 40px; top: 438px; width: 520px; height: 300px;
           background: linear-gradient(180deg, #f4f1ee 0%, #e9d6c6 45%, #d9b9a0 100%); border-radius: 4px; }

  .country-strip { position: absolute; left: 40px; top: 748px; width: 540px; color: var(--red);
                   font-size: 14.5px; line-height: 21px; }

  .footer-code { position: absolute; top: 812px; left: 40px; color: var(--red); font-family: "Noto Sans", sans-serif;
                 font-size: 17px; font-weight: 500; }
  .helpline { position: absolute; top: 803px; left: 220px; background: var(--cyan); color: var(--deep-blue);
              font-family: "Noto Sans", sans-serif; font-size: 20px; font-weight: 500; padding: 2px 10px; }

  .nb { position: absolute; left: 40px; top: 308px; width: 545px; font-size: 10.8px; line-height: 15px; color: var(--ink); }

  .countries { position: absolute; left: 40px; top: 386px; width: 520px; font-size: 11.6px;
               line-height: 18.3px; letter-spacing: 0.6px; color: var(--grey); text-align: justify; }

  .flag-grid { position: absolute; left: 38px; top: 511px; width: 520px; height: 157px;
               display: grid; grid-template-columns: repeat(9, 1fr); grid-template-rows: repeat(4, 1fr); gap: 4px; }
  .flag { background: var(--flag-red); }
  .flag--ar { background: linear-gradient(#74acdf 33%, #fff 33% 66%, #74acdf 66%); }
  .flag--au { background: #012169; }
  .flag--be { background: linear-gradient(90deg, #000 33%, #fdda24 33% 66%, #ef3340 66%); }
  .flag--br { background: #009c3b; }
  .flag--ca { background: linear-gradient(90deg, #d52b1e 25%, #fff 25% 75%, #d52b1e 75%); }
  .flag--cn { background: #de2910; }

  .terms-title { position: absolute; left: 40px; top: 690px; color: var(--deep-blue);
                 font-style: italic; font-weight: 600; font-size: 15px; line-height: 20px; }
  .terms { position: absolute; left: 40px; top: 711px; width: 540px; font-style: italic;
           font-size: 9.8px; line-height: 13.5px; color: var(--ink); }
</style>
</head>
<body>

<section class="page page--front">
  <div class="brand"><span class="brand__dot"></span>Orbit Telecom</div>

  <h1 class="headline">
    Make <strong>Unlimited Calls</strong><br>
    to <span class="big-num">40</span> Destinations<br>
    for just <strong>£10/month</strong>
  </h1>
  <span class="headline-bang">!</span>

  <h2 class="section-title" style="top:250px;">Subscribe via SMS Text Message:</h2>
  <ol class="steps steps--front">
    <li><b>1</b>. Text UNLSENDME to 68500.</li>
    <li><b>2</b>. You will receive a FREE Reply Message with details of our Unlimited Service</li>
    <li><b>3</b>. Confirm your subscription by replying AGREE to 68500.</li>
    <li><b>4</b>. You will then receive a Billed Premium SMS text message costing £10 + std. SMS.</li>
  </ol>

  <p class="para" style="top:350px;">To make a call dial <span class="hl">03445550187</span>. Upon hearing the prompts enter your full destination number followed by the # key on your mobile telephone keypad.</p>
  <p class="para" style="top:394px;">30 days after subscribing, you will receive another billed Premium SMS. This will occur every 30 days until you opt out. The next Call Package period starts on day 31st.</p>

  <div class="photo" role="img" aria-label="Group of smiling young people talking on mobile phones under speech bubbles filled with national flags"></div>

  <p class="country-strip">Australia, Canada, China, Denmark, France, Germany, Greece, Israel, Italy, Norway, Poland, Russia, South Korea, Spain, USA, India...</p>

  <div class="footer-code">UNLTELE</div>
  <div class="helpline">Customer Helpline - 0208 555 0143</div>
</section>

<section class="page page--back">
  <div class="brand"><span class="brand__dot"></span>Orbit Telecom</div>

  <h2 class="section-title" style="top:70px;">How the Service Works</h2>
  <ol class="steps steps--back">
    <li><b>1.</b> Send the SMS Text Message <span class="hl">UNLCCD</span> to <span class="hl">£10 Shortcode 68500.</span></li>
    <li><b>2.</b> You will receive a Free Reply Message with Details of our Service.</li>
    <li><b>3.</b> Opt into the service by sending a reply SMS text message <span class="hl">AGREE</span> to <span class="hl">68500</span></li>
    <li><b>4.</b> You will then receive a billed premium SMS text message costing £10.</li>
    <li><b>5.</b> You can start right away making unlimited calls to destinations included in the package.</li>
    <li><b>6.</b> 30 Days after previous successful SMS a new SMS MT Billed message is sent (occurs<br>&nbsp;&nbsp;&nbsp;&nbsp;every 30 days) until STOP command is received. (i.e. Text UNLOFF to 68500)</li>
    <li><b>7.</b> Next Call Package period starts on day 31 (which is now day 1 of a new period)</li>
    <li><b>8.</b> You will also receive a monthly free message containing Product Information.</li>
    <li><b>9.</b> To make a call, Dial <span class="hl">0344 555 0187 + 00 + Country Code + Destination Number</span></li>
    <li><b>10.</b> You may opt out at anytime by sending <span class="hl">UNLSTOP</span> to <span class="hl">68500</span></li>
  </ol>

  <p class="nb">N.B You can only subscribe to the service once in the same period from the same mobile number.<br>If you send a second request; a free message will be sent to advise that you have subscribed already.</p>

  <h2 class="section-title" style="top:356px;">Countries available with this offer include:</h2>
  <p class="countries">ARGENTINA, AUSTRALIA, BELGIUM, BRAZIL RIO AND SAO PAULO, CANADA (inc mobile), CHINA (inc mobile), COLOMBIA, DENMARK, CYPRUS SOUTH, FRANCE, GERMANY, GREECE, HONG KONG (inc mobile), HUNGARY, INDIA (inc mobile), IRELAND, ISRAEL, ITALY, MALAYSIA, NETHERLANDS, NEW ZEALAND, NORWAY, PORTUGAL, POLAND, RUSSIA, SINGAPORE, SOUTH KOREA, SPAIN, SWEDEN, SWITZERLAND, TAIWAN, THAILAND, TURKEY, USA (inc mobile).</p>

  <div class="flag-grid" role="img" aria-label="Grid of flags for the destination countries">
    <span class="flag flag--ar"></span><span class="flag flag--au"></span><span class="flag flag--be"></span>
    <span class="flag flag--br"></span><span class="flag flag--ca"></span><span class="flag flag--cn"></span>
    <span class="flag"></span><span class="flag"></span><span class="flag"></span>
    <span class="flag"></span><span class="flag"></span><span class="flag"></span><span class="flag"></span><span class="flag"></span><span class="flag"></span><span class="flag"></span><span class="flag"></span><span class="flag"></span>
    <span class="flag"></span><span class="flag"></span><span class="flag"></span><span class="flag"></span><span class="flag"></span><span class="flag"></span><span class="flag"></span><span class="flag"></span><span class="flag"></span>
    <span class="flag"></span><span class="flag"></span><span class="flag"></span><span class="flag"></span><span class="flag"></span><span class="flag"></span><span class="flag"></span><span class="flag"></span><span class="flag"></span>
  </div>

  <h3 class="terms-title">Terms and Conditions</h3>
  <p class="terms">T&amp;C: Ask bill payer's permission before using the service. Text to 68500 costs £10 plus your standard mobile network rates Our service is a subscription service and you will be charged £10 every 30 days; you may opt out at anytime by sending UNLSTOP to 68500. Calls to our 0344 555 0187 access number will be the same as 01 or 02 and charged at standard rate to a landline or included in your call package. Call duration is restricted to 60 minutes per call. Calls are subject to a fair usage policy. The service is not available to the Partner Network mobile customers. Service provider: Orbit Telecom Ltd. Helpline 02085550143.</p>

  <div class="footer-code">UNLTELE</div>
  <div class="helpline">Customer Helpline - 0208 555 0143</div>
</section>

</body>
</html>
```